Healthy Supplement featuring Moringa products

Need 3 business card options for our reps to order from Cardloom. Our reps will be ordering from Cardloom once we upload them. Attached is our current designs to show what info needs to be on the cards. Our website is www.tkvitality.com
The business cards will be a template for our reps to order from. Most of our reps are Asian & Hispanic. Please look at our website so you can see who we are to get the look and feel what we need.
Target Market(s)
Adults 30 on up. Health oriented people.
Industry/Entity Type
Health And Wellness
Contact Information for Business Card
Name
Title
Phone
Logo
www.tkvitality.com/my/username
Font styles to use
Requirements
Must have
- Please match our website look and colors. A moringa leaf is nice, but am open to something different.
Nice to have
- Healthy looking and warm, not super cold or too modern.
Should not have
- No harsh colors please.

```html
<!DOCTYPE html>
<html lang="en">
<head>
<meta charset="utf-8">
<title>TK Vitality – Business Card Options</title>
<link href="https://fonts.googleapis.com/css2?family=Cinzel:wght@500&family=Josefin+Sans:wght@400;600&display=swap" rel="stylesheet">
<style>
  :root {
    --board: #d6d6d6;
    --card: #ffffff;
    --leaf: #6aaa3f;
    --leaf-light: #8dc63f;
    --orange: #f58a2c;
    --ink: #1d1d1d;
    --sky: #8fa7a0;
    --rock: #c2865a;
    --pine: #2f4a2a;
  }
  * { margin: 0; padding: 0; box-sizing: border-box; }
  html, body { width: 1200px; height: 1200px; overflow: hidden; background: var(--board); }
  .board { position: relative; width: 1200px; height: 1200px; }
  .card {
    position: absolute; width: 408px; height: 264px; background: var(--card);
    overflow: hidden; box-shadow: 0 10px 22px rgba(0,0,0,.28);
    font-family: "Josefin Sans", sans-serif;
  }
  .card--banded  { left: 124px; top: 280px; }
  .card--photo   { left: 658px; top: 280px; }
  .card--gradient{ left: 124px; top: 646px; }
  .card--simple  { left: 658px; top: 646px; }

  .brand {
    position: absolute; font-family: "Cinzel", serif; font-weight: 500;
    color: var(--leaf); white-space: nowrap; text-align: center; line-height: 1;
    letter-spacing: .04em;
  }

  /* Option 1 */
  .band { position: absolute; top: 100px; height: 30px; }
  .band--left  { left: 4px; width: 62px; background: linear-gradient(90deg, rgba(106,170,63,.05), var(--leaf)); }
  .band--right { right: 4px; width: 62px; background: linear-gradient(90deg, var(--leaf), rgba(106,170,63,.05)); }
  .card--banded .brand { left: 74px; right: 74px; top: 101px; font-size: 27px; z-index: 1; }
  .contact-row {
    position: absolute; left: 24px; right: 18px; top: 208px;
    display: flex; justify-content: space-between; align-items: center;
    color: var(--orange); font-size: 9.5px;
  }
  .contact-row span { display: flex; align-items: center; gap: 5px; }
  .contact-row svg { width: 14px; height: 14px; }

  /* Option 2 */
  .scenery {
    position: absolute; left: 0; top: 0; width: 100%; height: 40px;
    background: linear-gradient(90deg, var(--pine) 0%, var(--sky) 22%, var(--rock) 55%, var(--pine) 100%);
  }
  .card--photo .brand { left: 18px; width: 170px; top: 140px; font-size: 22px; }
  .divider { position: absolute; left: 199px; top: 90px; width: 2px; height: 124px; background: var(--ink); }
  .details { position: absolute; left: 228px; top: 127px; font-size: 11px; color: var(--ink); letter-spacing: .04em; }
  .details div { display: flex; height: 17.5px; }
  .details dt { width: 30px; font-weight: 600; }

  /* Option 3 */
  .fade { position: absolute; left: 0; top: 0; width: 245px; height: 100%;
    background: linear-gradient(90deg, #ffffff 0%, #b6d39a 45%, var(--leaf) 100%); }
  .stripe { position: absolute; left: 245px; top: 0; width: 9px; height: 100%; background: var(--orange); }
  .card--gradient .brand { left: 254px; right: 0; top: 122px; font-size: 18px; }

  /* Option 4 */
  .card--simple .brand { left: 0; right: 0; top: 100px; font-size: 27px; }
  .web-line { position: absolute; left: 28px; right: 28px; top: 211px; display: flex; align-items: center; gap: 14px;
    font-size: 11px; color: var(--ink); letter-spacing: .05em; font-weight: 600; }
  .web-line::before, .web-line::after { content: ""; flex: 1; height: 1.5px; background: var(--ink); }
</style>
</head>
<body>
<main class="board">

  <section class="card card--banded" aria-label="Card option one">
    <div class="band band--left"></div>
    <div class="band band--right"></div>
    <div class="brand">TK VITALITY</div>
    <div class="contact-row">
      <span><svg viewBox="0 0 14 14"><circle cx="7" cy="7" r="7" fill="#f58a2c"/><path d="M4.5 4c.6 2.8 2.4 4.7 5 5.4l.8-1.2-1.4-.8-.7.6c-1-.5-1.7-1.3-2.1-2.3l.6-.7-.8-1.4z" fill="#fff"/></svg>(555) 014-2290</span>
      <span><svg viewBox="0 0 14 14"><circle cx="7" cy="7" r="7" fill="#f58a2c"/><rect x="3.5" y="4.5" width="7" height="5" fill="none" stroke="#fff"/><path d="M3.5 4.5 7 7.3l3.5-2.8" fill="none" stroke="#fff"/></svg>info@tkvitality.com</span>
      <span><svg viewBox="0 0 14 14"><circle cx="7" cy="7" r="7" fill="#f58a2c"/><circle cx="7" cy="7" r="3.6" fill="none" stroke="#fff" stroke-width=".9"/><path d="M3.4 7h7.2M7 3.4v7.2" stroke="#fff" stroke-width=".8"/></svg>www.tkvitality.com</span>
    </div>
  </section>

  <section class="card card--photo" aria-label="Card option two">
    <div class="scenery" role="img" aria-label="Photo strip of pine trees in front of a sunlit mountain"></div>
    <div class="brand">TK VITALITY</div>
    <div class="divider"></div>
    <dl class="details">
      <div><dt>P:</dt><dd>(555) 014-2290</dd></div>
      <div><dt>M:</dt><dd>info@tkvitality.com</dd></div>
      <div><dt>W:</dt><dd>www.tkvitality.com</dd></div>
    </dl>
  </section>

  <section class="card card--gradient" aria-label="Card option three">
    <div class="fade"></div>
    <div class="stripe"></div>
    <div class="brand">TK VITALITY</div>
  </section>

  <section class="card card--simple" aria-label="Card option four">
    <div class="brand">TK VITALITY</div>
    <div class="web-line">www.tkvitality.com</div>
  </section>

</main>
</body>
</html>
```